Biz cards, stationary, envelopes for Silver Meadow Church
Silver Meadow Church marketing package
Designers,
Thank all of you for your creativity and your contributions to this project. As our first project we are well pleased with the outcome and look forward to seeing you on future projects we post in the future.
Best wishes...
RT
Designers,just wanted to say all of you have submitted amazing drafts! For finalization, would like the "P" in logo to be the same brown color as "church." Some of you have already done so but this brings some consistency to the cards. Again nice designs! RT
KW/JRN/TD Team
Designers, can we have an option 2 for the back of the card under logo to read: 2 Cor. 5:18-20 (bold). Also please write "Church" in sentence case. Nice designs!!

```html
<!DOCTYPE html>
<html lang="en">
<head>
<meta charset="utf-8">
<title>Silver Meadow Church – Stationery Set</title>
<link href="https://fonts.googleapis.com/css2?family=Cinzel:wght@700&family=Open+Sans:wght@400;600&display=swap" rel="stylesheet">
<style>
  :root{
    --backdrop:#cfae85;
    --paper:#ffffff;
    --navy:#0d2f7a;
    --blue:#1f5fc4;
    --sky:#6fa7ea;
    --gold:#e0b53a;
    --gold-deep:#a9791a;
    --brown:#7a4a1e;
    --ink:#3b3b3b;
    --rule:#b9b9b9;
    --label:#ffffff;
  }
  *{box-sizing:border-box;margin:0;padding:0}
  html,body{width:1200px;height:674px;overflow:hidden}
  body{background:var(--backdrop);font-family:"Open Sans",sans-serif;color:var(--ink);position:relative}
  .piece{position:absolute;background:var(--paper);box-shadow:0 2px 6px rgba(0,0,0,.25);overflow:hidden}
  .piece-label{position:absolute;z-index:5;font-size:7px;font-weight:600;color:var(--label);text-align:center;white-space:nowrap;transform:translateX(-50%)}
  .piece-label.on-paper{color:var(--navy)}
  .brand{display:flex;flex-direction:column;align-items:center;gap:2px}
  .brand-mark{width:14px;height:14px;border-radius:50%;background:var(--blue)}
  .brand-name{font-family:"Cinzel",serif;font-weight:700;color:var(--navy);font-size:6px;letter-spacing:.3px;white-space:nowrap}
  .swoosh{position:absolute;left:0;bottom:0;width:100%}
  .contact{position:absolute;right:8px;bottom:4px;font-size:4.5px;line-height:1.4;color:#fff;text-align:right}
  .watermark{position:absolute;left:50%;top:50%;width:150px;height:150px;margin:-75px 0 0 -75px;border-radius:50%;border:16px solid rgba(31,95,196,.05)}

  /* business cards */
  .card{top:36px;width:152px;height:86px;border-radius:3px}
  .card-front .brand{position:absolute;left:10px;top:10px}
  .card-front .brand-name{font-size:5.5px}
  .card-front .details{position:absolute;right:8px;top:10px;width:36px;font-size:4px;line-height:1.5;text-align:right}
  .card-back{display:flex;align-items:center;justify-content:center}
  .card-back.blue{background:radial-gradient(circle at 50% 40%,var(--sky),var(--blue) 55%,var(--navy))}
  .card-back.gold{background:radial-gradient(circle at 50% 40%,#fbe58a,var(--gold) 55%,var(--gold-deep))}
  .card-back .brand-mark{width:26px;height:26px}
  .card-back.blue .brand-mark{background:#fff}
  .card-back.gold .brand-mark{background:var(--navy)}

  /* fax & letterhead */
  .sheet{top:151px;width:342px;height:497px}
  .sheet .brand{position:absolute;left:0;right:0;top:12px}
  .sheet .brand-mark{width:20px;height:20px}
  .sheet .brand-name{font-size:8px}
  .fax-title{position:absolute;right:16px;top:50px;font-size:9px;font-weight:600;color:var(--navy)}
  .fax-table{position:absolute;left:16px;right:16px;top:62px;border-collapse:collapse;font-size:5.5px}
  .fax-table td{border:1px solid var(--rule);height:13px;padding:0 3px}
  .fax-table .field-label{width:24px;color:var(--ink)}
  .fax-table .field-value{background:#f2f2f2}
  .fax-options{position:absolute;left:16px;right:16px;top:122px;display:flex;justify-content:space-between;font-size:5px}
  .fax-options span::before{content:"";display:inline-block;width:5px;height:5px;border:1px solid var(--rule);margin-right:3px;vertical-align:-1px}

  /* envelopes */
  .envelope-front{left:766px;top:55px;width:403px;height:197px}
  .envelope-front .brand{position:absolute;left:14px;top:12px;align-items:flex-start}
  .envelope-front .brand-mark{width:20px;height:20px}
  .envelope-front .brand-name{font-size:7px}
  .envelope-back{left:766px;width:403px;height:144px}
  .envelope-back svg.flap{position:absolute;left:0;top:0;width:100%;height:70px}
  .envelope-back .brand{position:absolute;left:0;right:0;top:14px}
  .envelope-back .brand-mark{width:20px;height:20px}
</style>
</head>
<body>

<svg width="0" height="0" style="position:absolute" aria-hidden="true">
  <defs>
    <linearGradient id="blueBand" x1="0" y1="0" x2="1" y2="0">
      <stop offset="0" stop-color="#0d2f7a"/><stop offset=".5" stop-color="#1f5fc4"/><stop offset="1" stop-color="#6fa7ea"/>
    </linearGradient>
    <linearGradient id="goldBand" x1="0" y1="0" x2="1" y2="0">
      <stop offset="0" stop-color="#a9791a"/><stop offset=".5" stop-color="#f3d063"/><stop offset="1" stop-color="#a9791a"/>
    </linearGradient>
    <radialGradient id="blueFlap" cx=".5" cy=".2" r=".8">
      <stop offset="0" stop-color="#6fa7ea"/><stop offset=".6" stop-color="#1f5fc4"/><stop offset="1" stop-color="#0d2f7a"/>
    </radialGradient>
    <radialGradient id="goldFlap" cx=".5" cy=".2" r=".8">
      <stop offset="0" stop-color="#fbe58a"/><stop offset=".6" stop-color="#e0b53a"/><stop offset="1" stop-color="#a9791a"/>
    </radialGradient>
  </defs>
</svg>

<!-- labels -->
<div class="piece-label" style="left:129px;top:24px">Business Card (Front)</div>
<div class="piece-label" style="left:298px;top:24px">Business Card (Back) Option 1</div>
<div class="piece-label" style="left:459px;top:24px">Business Card (Back) Option 2</div>
<div class="piece-label" style="left:624px;top:24px">Business Card (Back) Option 3</div>
<div class="piece-label" style="left:202px;top:140px">Fax Cover</div>
<div class="piece-label" style="left:562px;top:140px">Letterhead</div>
<div class="piece-label" style="left:967px;top:43px">Envelope (Front)</div>
<div class="piece-label" style="left:967px;top:266px">Envelope (Back) Option 1</div>
<div class="piece-label on-paper" style="left:967px;top:355px">Envelope (Back) Option 2</div>
<div class="piece-label on-paper" style="left:967px;top:444px">Envelope (Back) Option 3</div>

<!-- business card front -->
<div class="piece card card-front" style="left:53px">
  <div class="brand"><div class="brand-mark"></div><div class="brand-name">Silver Meadow Church</div></div>
  <div class="details">Pastor Name<br>Senior Pastor<br>555 014 2200<br>silvermeadow.org</div>
  <svg class="swoosh" viewBox="0 0 400 60" height="30" preserveAspectRatio="none" aria-hidden="true">
    <path d="M0 32 Q200 2 400 16 L400 60 L0 60Z" fill="url(#blueBand)"/>
    <path d="M0 28 Q200 -2 400 12" fill="none" stroke="url(#goldBand)" stroke-width="4"/>
  </svg>
</div>

<div class="piece card card-back" style="left:223px">
  <div class="brand"><div class="brand-mark"></div><div class="brand-name">Silver Meadow Church</div></div>
  <svg class="swoosh" viewBox="0 0 400 60" height="26" preserveAspectRatio="none" aria-hidden="true">
    <path d="M0 32 Q200 2 400 16 L400 60 L0 60Z" fill="url(#blueBand)"/>
    <path d="M0 28 Q200 -2 400 12" fill="none" stroke="url(#goldBand)" stroke-width="4"/>
  </svg>
</div>
<div class="piece card card-back blue" style="left:384px"><div class="brand-mark"></div></div>
<div class="piece card card-back gold" style="left:550px"><div class="brand-mark"></div></div>

<!-- fax cover -->
<div class="piece sheet fax-cover" style="left:31px">
  <div class="watermark"></div>
  <div class="brand"><div class="brand-mark"></div><div class="brand-name">Silver Meadow Church</div></div>
  <div class="fax-title">FAX</div>
  <table class="fax-table">
    <tr><td class="field-label">To:</td><td class="field-value"></td><td class="field-label">From:</td><td class="field-value"></td></tr>
    <tr><td class="field-label">Fax:</td><td class="field-value"></td><td class="field-label">Pages:</td><td class="field-value"></td></tr>
    <tr><td class="field-label">Phone:</td><td class="field-value"></td><td class="field-label">Date:</td><td class="field-value"></td></tr>
    <tr><td class="field-label">Re:</td><td class="field-value"></td><td class="field-label">CC:</td><td class="field-value"></td></tr>
  </table>
  <div class="fax-options"><span>Urgent</span><span>For Review</span><span>Please Comment</span><span>Please Reply</span><span>Please Recycle</span></div>
  <svg class="swoosh" viewBox="0 0 400 60" height="48" preserveAspectRatio="none" aria-hidden="true">
    <path d="M0 32 Q200 2 400 16 L400 60 L0 60Z" fill="url(#blueBand)"/>
    <path d="M0 28 Q200 -2 400 12" fill="none" stroke="url(#goldBand)" stroke-width="3"/>
  </svg>
  <div class="contact">12 Meadow Lane<br>Rivertown, TX 75001<br>555 014 2200<br>info@silvermeadow.org</div>
</div>

<!-- letterhead -->
<div class="piece sheet letterhead" style="left:391px">
  <div class="watermark"></div>
  <div class="brand"><div class="brand-mark"></div><div class="brand-name">Silver Meadow Church</div></div>
  <svg class="swoosh" viewBox="0 0 400 60" height="48" preserveAspectRatio="none" aria-hidden="true">
    <path d="M0 32 Q200 2 400 16 L400 60 L0 60Z" fill="url(#blueBand)"/>
    <path d="M0 28 Q200 -2 400 12" fill="none" stroke="url(#goldBand)" stroke-width="3"/>
  </svg>
  <div class="contact">12 Meadow Lane<br>Rivertown, TX 75001<br>555 014 2200<br>info@silvermeadow.org</div>
</div>

<!-- envelope front -->
<div class="piece envelope-front">
  <div class="brand"><div class="brand-mark"></div><div class="brand-name">Silver Meadow Church</div></div>
  <svg class="swoosh" viewBox="0 0 400 60" height="42" preserveAspectRatio="none" aria-hidden="true">
    <path d="M0 32 Q200 2 400 16 L400 60 L0 60Z" fill="url(#blueBand)"/>
    <path d="M0 28 Q200 -2 400 12" fill="none" stroke="url(#goldBand)" stroke-width="3"/>
  </svg>
</div>

<!-- envelope backs -->
<div class="piece envelope-back" style="top:278px">
  <svg class="flap" viewBox="0 0 400 70" preserveAspectRatio="none" aria-hidden="true">
    <path d="M0 0 L200 62 L400 0Z" fill="#fff" stroke="#d6d6d6" stroke-width="1"/>
  </svg>
  <div class="brand"><div class="brand-mark"></div><div class="brand-name">Silver Meadow Church</div></div>
</div>
<div class="piece envelope-back" style="top:367px">
  <svg class="flap" viewBox="0 0 400 70" preserveAspectRatio="none" aria-hidden="true">
    <path d="M0 0 L200 62 L400 0Z" fill="url(#blueFlap)"/>
    <path d="M0 0 L200 62 L400 0" fill="none" stroke="url(#goldBand)" stroke-width="2"/>
  </svg>
  <div class="brand" style="top:30px"><div class="brand-mark" style="background:#fff"></div></div>
</div>
<div class="piece envelope-back" style="top:456px">
  <svg class="flap" viewBox="0 0 400 70" preserveAspectRatio="none" aria-hidden="true">
    <path d="M0 0 L200 62 L400 0Z" fill="url(#goldFlap)"/>
    <path d="M0 0 L200 62 L400 0" fill="none" stroke="#0d2f7a" stroke-width="2"/>
  </svg>
  <div class="brand" style="top:30px"><div class="brand-mark"></div></div>
</div>

</body>
</html>
```